Book cover design about quality management systems

Book cover design that I can display in my website for ore orders
The book is about helping organisations to fully integrate their Quality management systems rather than having a quality system which sits off to the side and adds extra work.
It is aimed at organisations leaders
It is about leaders taking ownership and leading the decision and design of the quality management system and therefore being able to delegate more effectively.

Target Market(s)

CEO of government funded organisations

Industry/Entity Type

Management

Font styles to use
Sans Serif

Colors

Designer to choose colors to be used in the design.

Requirements
Must have
• Ability to be used on website
• Title of the book
• Shape steer sustain
• Strap line - Building quality into the work
Nice to have
• Not too fussy
• Not a black cover
• Deep Yellow in the design if possible
Should not have
• Anything too feminine

```html
<!DOCTYPE html>
<html lang="en">
<head>
<meta charset="utf-8">
<title>Shape Steer Sustain — Book Cover</title>
<link rel="stylesheet" href="https://fonts.googleapis.com/css2?family=Oswald:wght@500;700&family=Roboto+Condensed:wght@300;700&display=swap">
<style>
  :root {
    --backdrop: #e9e9e9;
    --paper: #ffffff;
    --ink: #111111;
    --gold: #efc43a;
    --gold-soft: #f7dc82;
    --rule: #444444;
  }
  * { margin: 0; padding: 0; box-sizing: border-box; }
  html, body {
    width: 1200px;
    height: 1200px;
    overflow: hidden;
    background: radial-gradient(circle at 50% 45%, #ffffff 0%, var(--backdrop) 100%);
  }
  .cover {
    position: absolute;
    left: 230px;
    top: 45px;
    width: 740px;
    height: 1110px;
    background: var(--paper);
    box-shadow: 0 10px 40px rgba(0,0,0,0.12);
    overflow: hidden;
  }
  .network-art {
    position: absolute;
    left: 0;
    top: 0;
    width: 740px;
    height: 760px;
  }
  .title-block {
    position: absolute;
    left: 100px;
    top: 420px;
    width: 560px;
    height: 380px;
    font-weight: normal;
  }
  .title-initial {
    position: absolute;
    left: 0;
    top: -3px;
    font-family: "Oswald", sans-serif;
    font-weight: 700;
    font-size: 380px;
    line-height: 1;
    color: var(--gold);
  }
  .title-word {
    position: absolute;
    left: 178px;
    font-family: "Oswald", sans-serif;
    font-weight: 700;
    color: var(--ink);
    line-height: 1;
    text-transform: uppercase;
    white-space: nowrap;
  }
  .title-word--shape   { top: 33px;  font-size: 118px; letter-spacing: 30px; }
  .title-word--steer   { top: 165px; font-size: 76px;  letter-spacing: 48px; font-weight: 500; }
  .title-word--sustain { top: 253px; font-size: 118px; letter-spacing: 2px; }
  .title-rule {
    position: absolute;
    left: 100px;
    top: 800px;
    width: 560px;
    height: 2px;
    background: var(--rule);
  }
  .strapline {
    position: absolute;
    left: 100px;
    top: 812px;
    width: 560px;
    font-family: "Roboto Condensed", sans-serif;
    font-weight: 300;
    font-size: 33px;
    letter-spacing: 1px;
    color: var(--ink);
    text-transform: uppercase;
    white-space: nowrap;
  }
  .author {
    position: absolute;
    left: 100px;
    top: 925px;
    width: 560px;
    font-family: "Roboto Condensed", sans-serif;
    font-weight: 700;
    font-size: 46px;
    letter-spacing: 2px;
    color: var(--ink);
    text-transform: uppercase;
    text-align: center;
    white-space: nowrap;
  }
</style>
</head>
<body>
  <main class="cover">
    <svg class="network-art" viewBox="0 0 740 760" role="img" aria-label="Connected network of thin gold lines and dots spreading from the top right across the upper cover">
      <defs>
        <linearGradient id="networkTone" x1="1" y1="0" x2="0" y2="1">
          <stop offset="0" stop-color="var(--gold-soft)" stop-opacity="0.55"/>
          <stop offset="1" stop-color="var(--gold-soft)" stop-opacity="0.12"/>
        </linearGradient>
      </defs>
      <polygon points="260,0 740,0 740,260 560,300 420,330 300,420 180,560 90,720 0,760 0,560 60,420 140,300 200,140" fill="url(#networkTone)"/>
    </svg>

    <h1 class="title-block" aria-label="Shape Steer Sustain">
      <span class="title-initial">S</span>
      <span class="title-word title-word--shape">hape</span>
      <span class="title-word title-word--steer">teer</span>
      <span class="title-word title-word--sustain">ustain</span>
    </h1>

    <div class="title-rule"></div>
    <p class="strapline">Building quality into the work</p>
    <p class="author">Margaret Holloway</p>
  </main>
</body>
</html>
```